"Velvet Harbor - The Musical" Poster

I need a poster design for a new musical called "Velvet Harbor", based on the classic 1984 film of the same title.
The pictures I've attached were used to advertise the original film. They might help get an idea.
Updates
Hi designers!
IMPORTANT UPDATE!! PLEASE READ!!
Hi everyone!
Hi everyone!
Target Market(s)
Ticket buying audience
Requirements
Must have
- * "Velvet Harbor - The Musical"
* A new musical by Colin Marsh
* Based on the classic film "Velvet Harbor" written by Oscar Pellington.
* A space at the top and the bottom of the poster for additional details that can be added later.
* A graphical title visual that can be used for further promotion.
* A picture/visual representing the musical
Nice to have
- * something equally 80's but also modern.
Should not have
- * be a direct copy of the original film poster designs but reflect them in some way

```html
<!DOCTYPE html>
<html lang="en">
<head>
<meta charset="utf-8">
<title>Velvet Harbor - The Musical</title>
<link href="https://fonts.googleapis.com/css2?family=Bungee+Outline&family=Kaushan+Script&family=Montserrat:wght@500;600&display=swap" rel="stylesheet">
<style>
  :root {
    --night: #000000;
    --ember: #8a2a0a;
    --plum: #4a1a5e;
    --gold: #d9a21a;
    --neon-pink: #ff3aa8;
    --neon-red: #ff2a3a;
    --magenta: #ff1f9a;
    --tab-orange: #ff5a12;
    --credit: #f4c8dc;
  }
  html, body {
    margin: 0;
    padding: 0;
    overflow: hidden;
    background: var(--night);
  }
  .poster {
    position: relative;
    width: 927px;
    height: 1200px;
    overflow: hidden;
    background: var(--night);
  }
  .key-visual {
    position: absolute;
    inset: 0;
    background:
      radial-gradient(circle at 22% 22%, rgba(120, 200, 40, 0.35) 0 4%, transparent 12%),
      radial-gradient(ellipse at 50% 25%, rgba(110, 40, 140, 0.55) 0%, transparent 40%),
      radial-gradient(ellipse at 40% 35%, rgba(138, 42, 10, 0.55) 0%, transparent 45%),
      radial-gradient(circle at 75% 58%, rgba(217, 140, 26, 0.45) 0%, transparent 22%),
      radial-gradient(circle at 10% 10%, rgba(217, 162, 26, 0.3) 0%, transparent 18%),
      radial-gradient(ellipse at 50% 85%, rgba(60, 20, 10, 0.6) 0%, transparent 50%),
      var(--night);
  }
  .credit-top {
    position: absolute;
    left: 0;
    right: 0;
    top: 706px;
    margin: 0;
    text-align: center;
    font-family: "Montserrat", sans-serif;
    font-weight: 600;
    font-size: 17px;
    letter-spacing: 4px;
    text-transform: uppercase;
    color: var(--credit);
    text-shadow: 0 0 6px rgba(255, 58, 168, 0.5);
  }
  .title {
    position: absolute;
    left: 0;
    right: 0;
    top: 745px;
    margin: 0;
    text-align: center;
    font-family: "Bungee Outline", sans-serif;
    font-weight: 400;
    font-size: 136px;
    line-height: 150px;
    letter-spacing: 4px;
    color: var(--neon-pink);
    text-shadow:
      0 0 2px var(--neon-red),
      0 0 6px var(--neon-red),
      0 0 14px rgba(255, 42, 58, 0.7),
      0 0 28px rgba(255, 58, 168, 0.5);
  }
  .title span { display: block; }
  .subtitle {
    position: absolute;
    left: 0;
    right: 0;
    top: 1062px;
    margin: 0;
    text-align: center;
    font-family: "Kaushan Script", cursive;
    font-size: 40px;
    line-height: 50px;
    color: var(--magenta);
    text-shadow: 0 0 6px rgba(255, 31, 154, 0.5);
  }
  .details-tab {
    position: absolute;
    left: 288px;
    top: 1105px;
    width: 351px;
    height: 95px;
  }
  .credit-bottom {
    position: absolute;
    left: 308px;
    width: 311px;
    top: 1160px;
    margin: 0;
    text-align: center;
    font-family: "Montserrat", sans-serif;
    font-weight: 500;
    font-size: 11.5px;
    line-height: 16px;
    color: var(--credit);
  }
</style>
</head>
<body>
  <main class="poster">
    <div class="key-visual" role="img" aria-label="Abstract neon illustration: glowing bokeh lights, purple and red smoke swirls and sparkling stars on black"></div>
    <p class="credit-top">A new musical by Colin Marsh</p>
    <h1 class="title"><span>Velvet</span><span>Harbor</span></h1>
    <p class="subtitle">The Musical</p>
    <svg class="details-tab" viewBox="0 0 390 95" preserveAspectRatio="none" aria-hidden="true">
      <defs>
        <linearGradient id="tabEdge" x1="0" y1="0" x2="0" y2="1">
          <stop offset="0" stop-color="#ff7a20"/>
          <stop offset="1" stop-color="#e0301a"/>
        </linearGradient>
      </defs>
      <path d="M4 0 C8 22 18 30 40 32 H350 C372 30 382 22 386 0 C392 30 388 44 372 52 C360 58 350 60 350 60 H40 C40 60 30 58 18 52 C2 44 -2 30 4 0 Z"
            fill="url(#tabEdge)"/>
      <path d="M14 95 V70 C14 56 26 46 40 46 H350 C364 46 376 56 376 70 V95 Z"
            fill="var(--night)" stroke="url(#tabEdge)" stroke-width="5"/>
    </svg>
    <p class="credit-bottom">Based on the classic film &ldquo;Velvet Harbor&rdquo;<br>written by Oscar Pellington</p>
  </main>
</body>
</html>
```